New Consulting Firm News PowerPoint Template

We are a new consulting firm that specializes in Veltrix Unified Results Planning implementations in need of a new PowerPoint template. We need at least the following layouts:
• Main Cover Slide
• Agenda / Table of Contents
• Title slide for each of the agenda items leading into actual content
• Title + Content with nice bullets in the content
• Title + Sub-Title + Content with nice bullets in the content
• Title + Two Columns of Content
• Title + Sub-Title + Two Columns of Content
• Title + Three Columns of Content
• Title + Sub-Title + Three Columns of Content
• Title + Two Rows and Two Columns of Content (4 boxes)
• Title + Sub-Title + Two Rows and Two Columns of Content (4 boxes)
• Title + Blank
• Nascar Slide (Client logos arranged somehow)
• Case Study Slide
• Various infographic slides than can be used and modified would be amazing as well
Our logo has been uploaded and you can find our website here:
https://brankelladvisory.example
We would like the main theme colors to blend with our logo, but also have a variety of colors in the theme that compliment the main theme colors. Once we have selected a PowerPoint design we expect to immediately have a Word design contest and the winning PowerPoint design will likely be a heavy influence on the Word design.

Target Market(s)

CFO, CAO, VP of Finance, Controllers

Industry/Entity Type

Consulting

Font styles to use
Serif
Sans Serif

Requirements
Must have
• • Main Cover Slide
• Title + Blank
• Case Study Slide
Nice to have
• • Various infographic slides than can be used and modified would be amazing as well

```html
<!DOCTYPE html>
<html lang="en">
<head>
<meta charset="utf-8">
<title>Brankell Advisory – Presentation Template</title>
<link rel="stylesheet" href="https://fonts.googleapis.com/css2?family=Montserrat:wght@400;500;600;700&family=Poppins:wght@500;600;700&display=swap">
<style>
:root{
  --blue:#1f74c0;
  --navy:#27377a;
  --gray:#6b6d70;
  --dark:#4a4b4e;
  --ink:#222428;
  --text:#555a60;
  --mute:#9a9ea3;
  --pale:#e8eff8;
  --line:#e2e5e9;
  --canvas:#e9eaec;
}
*{box-sizing:border-box}
html,body{margin:0;padding:0}
body{width:1200px;height:2266px;overflow:hidden;background:var(--canvas);font-family:Montserrat,sans-serif;color:var(--text)}
.deck{display:grid;grid-template-columns:repeat(3,390px);grid-auto-rows:219px;gap:6px;padding:10px 9px 12px;width:1200px;height:2266px}
.slide{position:relative;overflow:hidden;background:#fff}
.abs{position:absolute}
.mark{position:absolute;left:7px;top:8px;width:9px;height:9px;border-radius:2px;background:var(--blue)}
.vurl{position:absolute;left:9px;top:62px;writing-mode:vertical-rl;transform:rotate(180deg);font-size:3px;letter-spacing:.7px;color:#b5b8bc}
.pno{position:absolute;left:7px;bottom:8px;width:10px;height:10px;border-radius:50%;background:var(--blue);color:#fff;font-size:4px;display:flex;align-items:center;justify-content:center}
.title{position:absolute;left:28px;top:24px;margin:0;font-family:Poppins,sans-serif;font-weight:600;font-size:15px;color:var(--ink);white-space:nowrap}
.title.center{left:0;right:0;text-align:center}
.subtitle{position:absolute;margin:0;font-size:6.5px;letter-spacing:1.6px;color:var(--blue);white-space:nowrap}
.subtitle.center{left:0;right:0;text-align:center}
.para{margin:0;font-size:4.4px;line-height:1.45;color:var(--text);text-align:justify}
.para + .para{margin-top:5px}
.brand{position:absolute;display:flex;align-items:center;gap:5px;font-family:Montserrat,sans-serif;font-weight:600;color:var(--blue);white-space:nowrap}
.brand-sq{display:inline-block;border-radius:2px;background:currentColor}
.photo{position:absolute}
/* covers */
.cover-url{position:absolute;left:18px;top:44px;font-size:4.5px;letter-spacing:2.4px;font-weight:600}
.cover-title{position:absolute;left:15px;top:96px;margin:0;font-family:Montserrat,sans-serif;font-weight:700;font-size:15px;line-height:.98;letter-spacing:-.2px}
.cover-sub{position:absolute;left:15px;top:127px;font-size:9px;letter-spacing:1.5px}
.cover-date{position:absolute;left:18px;top:181px;font-size:5.5px;font-weight:600}
.hero-title{position:absolute;margin:0;font-family:Poppins,sans-serif;font-weight:600;font-size:16px;line-height:1.1}
.hero-sub{position:absolute;font-size:5.5px;letter-spacing:1.6px}
.hero-url{position:absolute;font-size:7px}
.chapter-title{position:absolute;left:25px;top:90px;margin:0;font-family:Poppins,sans-serif;font-weight:600;font-size:17px}
.chapter-sub{position:absolute;left:25px;top:111px;font-weight:700;font-size:11px;letter-spacing:.3px}
.chapter-text{position:absolute;left:25px;top:135px;width:170px;font-size:4.3px;line-height:1.35}
/* agenda */
.agenda-panel{position:absolute;left:0;top:0;width:166px;height:219px;background:var(--blue)}
.agenda-list{position:absolute;left:202px;top:46px;width:160px;margin:0;padding:0;list-style:none}
.agenda-list li{display:flex;height:15.6px;align-items:center;border-bottom:.6px solid var(--line);font-size:6px;color:var(--text)}
.agenda-list li span{width:24px;color:var(--mute)}
/* bullets */
.bullets{margin:0;padding:0;list-style:none}
.bullets li{position:relative;padding-left:9px;font-size:4.4px;line-height:1.45;color:var(--text)}
.bullets li::before{content:"";position:absolute;left:0;top:1px;width:4px;height:4px;border-radius:50%;background:var(--blue)}
.bullets.big li{padding-left:12px;margin-bottom:8px}
.bullets.big li::before{width:6px;height:6px;top:0;box-shadow:0 0 0 1.2px #cfe0f2}
.bullets.small li{margin-bottom:5px;white-space:nowrap}
/* cards */
.card{position:absolute;width:100px;height:130px;background:#fff;border-top:2.5px solid var(--blue);box-shadow:0 1px 5px rgba(0,0,0,.12);text-align:center;padding:10px 7px 0}
.card .icon{width:28px;height:28px;border-radius:50%;background:var(--blue);margin:0 auto 10px;box-shadow:0 0 0 3px #dce8f5;display:flex;align-items:center;justify-content:center}
.card h4{margin:0 0 3px;font-size:5.3px;font-weight:700;color:var(--ink)}
.card .para{font-size:4.1px;text-align:justify}
.cols{position:absolute;display:flex;gap:14px}
.cols > div{flex:1}
.box{position:absolute;width:146px;height:50px;background:#fff;box-shadow:0 1px 4px rgba(0,0,0,.12);border-left:3px solid var(--navy);padding:7px 12px}
.box.gray{border-left-color:var(--gray)}
.box h4{margin:0 0 4px;font-size:5px;font-weight:700;color:var(--ink)}
.box .para{font-size:4.3px}
/* two-by-two table */
.split{position:absolute;left:38px;top:75px;width:327px;display:grid;grid-template-columns:1fr 1fr}
.split .head{height:23px;display:flex;align-items:center;justify-content:center;color:#fff;font-size:7px;font-weight:600;letter-spacing:.3px}
.split .cell{height:50px;border-bottom:.6px solid var(--line);text-align:center;padding:6px 10px}
.split .cell h4{margin:0 0 3px;font-size:6px;font-weight:700;color:var(--ink)}
.split .cell p{margin:0;font-size:4px;line-height:1.35}
/* nascar */
.client{position:absolute;width:52px;height:23px;background:#fff;border-radius:2px;box-shadow:0 1px 4px rgba(0,0,0,.14);display:flex;align-items:center;justify-content:center;font-size:7px;font-weight:700;color:#333a42}
/* case study */
.band{position:absolute;top:148px;width:130px;height:71px;padding:26px 14px 0;color:#fff}
.band h4{margin:0 0 2px;font-size:6.5px;font-weight:600}
.band p{margin:0;font-size:4.3px;line-height:1.35}
.badge{position:absolute;top:132px;width:28px;height:28px;border-radius:50%;display:flex;align-items:center;justify-content:center}
/* data table */
.grid-table{position:absolute;left:30px;top:67px;border-collapse:collapse;font-size:4.5px}
.grid-table th{background:var(--blue);color:#fff;font-weight:600;height:15px;width:60px;border-right:.6px solid #4f93d0}
.grid-table th.blank{background:none;width:95px;border:0}
.grid-table td{height:15px;text-align:center;border-bottom:.6px solid var(--line);color:#444}
.grid-table td.label{background:var(--dark);color:#fff;font-weight:600;border-bottom:.6px solid #6a6b6e}
/* numbered list */
.step{position:absolute;left:210px;width:160px;display:flex;gap:7px}
.step .num{flex:none;width:13px;height:13px;border-radius:50%;background:var(--blue);color:#fff;font-size:5px;font-weight:700;display:flex;align-items:center;justify-content:center;box-shadow:0 0 0 1.5px #cfe0f2}
.step h4{margin:0 0 1px;font-size:5px;font-weight:700;color:var(--ink)}
.step p{margin:0;font-size:4px;line-height:1.3}
.tl-label{position:absolute;width:70px;text-align:center;font-size:4.3px;line-height:1.3;color:var(--text)}
.tl-label b{display:block;color:var(--ink);font-size:4.8px}
.money{position:absolute;font-family:Poppins,sans-serif;font-weight:600;font-size:9px;color:var(--ink)}
.check{position:absolute;left:248px;display:flex;gap:8px;width:125px}
.check h4{margin:0 0 1px;font-size:4.8px;font-weight:700;color:var(--ink)}
.check p{margin:0;font-size:4.2px;line-height:1.3}
.node{position:absolute;width:80px;font-size:4px;line-height:1.35;color:var(--mute)}
.node b{display:block;color:var(--ink);font-size:5px}
.node.right{text-align:left}
.node.left{text-align:left}
.stage{position:absolute;left:160px;top:90px;width:70px;height:70px;border-radius:14px;background:var(--blue);transform:rotate(45deg)}
.stage-text{position:absolute;left:150px;top:110px;width:90px;text-align:center;color:#fff;font-size:4px;line-height:1.5}
.stage-text b{display:block;font-size:6.5px;font-weight:600;margin-bottom:2px}
.side-note{position:absolute;width:90px;font-size:4.3px;line-height:1.35;text-align:center}
.side-note b{display:block;color:var(--ink);font-size:5px;margin-bottom:1px}
.item{position:absolute;display:flex;gap:9px;width:160px}
.item .ic{flex:none;width:22px;height:22px;border-radius:50%;display:flex;align-items:center;justify-content:center}
.item h4{margin:0 0 2px;font-size:5px;font-weight:700;color:var(--ink)}
.item p{margin:0;font-size:4.3px;line-height:1.35}
.tri-text{position:absolute;width:54px;text-align:center;color:#fff;font-size:3.5px;line-height:1.3}
.tri-text b{display:block;font-size:5px;margin-bottom:1px}
.contact-card{position:absolute;left:54px;top:52px;width:104px;background:#fff;box-shadow:0 1px 5px rgba(0,0,0,.12)}
.contact-card .row{height:24px;display:flex;align-items:center;gap:9px;padding-left:9px;font-size:4px;color:var(--text);border-bottom:.6px solid var(--line)}
.contact-card .row.lead{background:var(--blue);color:#fff}
.socials{position:absolute;left:80px;top:190px;display:flex;gap:3px}
.socials span{width:7px;height:7px;border-radius:1.5px;background:var(--blue)}
</style>
</head>
<body>
<main class="deck">

<!-- 1 cover light -->
<section class="slide">
  <div class="cover-url" style="color:#777">WWW.BRANKELLADVISORY.EXAMPLE</div>
  <h1 class="cover-title" style="color:var(--blue)">PRESENTATION<br>TITLE GOES HERE</h1>
  <div class="cover-sub" style="color:var(--gray)">SUB TITLE GOES HERE</div>
  <div class="cover-date" style="color:var(--blue)">March 2021</div>
  <div class="brand" style="left:232px;top:136px;font-size:15px"><span class="brand-sq" style="width:14px;height:14px"></span>Brankell Advisory</div>
</section>

<!-- 2 cover blue -->
<section class="slide" style="background:var(--blue);color:#fff">
  <div class="cover-url">WWW.BRANKELLADVISORY.EXAMPLE</div>
  <h1 class="cover-title">PRESENTATION<br>TITLE GOES HERE</h1>
  <div class="cover-sub">SUB TITLE GOES HERE</div>
  <div class="cover-date">March 2021</div>
  <div class="brand" style="left:232px;top:136px;font-size:15px;color:#fff"><span class="brand-sq" style="width:14px;height:14px"></span>Brankell Advisory</div>
</section>

<!-- 3 hero light -->
<section class="slide" style="background:#f1f2f4">
  <div class="photo" role="img" aria-label="Glass office towers seen from below" style="left:232px;top:0;width:158px;height:219px;background:linear-gradient(160deg,#c9d3de,#5f7ea0 55%,#2d4f78)"></div>
  <div class="brand" style="left:28px;top:40px;font-size:6px"><span class="brand-sq" style="width:7px;height:7px"></span>Brankell Advisory</div>
  <h2 class="hero-title" style="left:27px;top:88px;color:var(--blue)">Your Presentation<br>Title Goes Here</h2>
  <div class="hero-sub" style="left:28px;top:128px;color:var(--mute)">SUBTITLE GOES HERE</div>
  <div class="hero-url" style="left:27px;top:188px;color:var(--gray)">brankelladvisory.example</div>
</section>

<!-- 4 hero dark -->
<section class="slide">
  <div class="photo" role="img" aria-label="Dark city skyline with office towers" style="inset:0;background:linear-gradient(135deg,#1c1d20,#2b2e33 45%,#3e5d80 75%,#1b2a3d)"></div>
  <div class="brand" style="left:28px;top:40px;font-size:6px"><span class="brand-sq" style="width:7px;height:7px"></span>Brankell Advisory</div>
  <h2 class="hero-title" style="left:27px;top:88px;color:var(--blue)">Your Presentation<br>Title Goes Here</h2>
  <div class="hero-sub" style="left:28px;top:128px;color:#fff">SUBTITLE GOES HERE</div>
  <div class="hero-url" style="left:27px;top:188px;color:#fff">brankelladvisory.example</div>
</section>

<!-- 5 chapter blue -->
<section class="slide" style="background:var(--blue);color:#fff">
  <div class="brand" style="left:25px;top:46px;font-size:6px;color:#fff"><span class="brand-sq" style="width:7px;height:7px"></span>Brankell Advisory</div>
  <h2 class="chapter-title">Chapter Devider</h2>
  <div class="chapter-sub">INTRODUCTION</div>
  <p class="chapter-text">Lorem ipsum dolor sit amet, consectetur adipiscing elit, sed do eiusmod tempor incididunt ut labore et dolore magna aliqua. Lorem ipsum dolor sit amet, consectetur adipiscing elit, sed do eiusmod tempor incididunt ut labore et dolore magna aliqua.</p>
</section>

<!-- 6 chapter light -->
<section class="slide">
  <div class="brand" style="left:25px;top:46px;font-size:6px"><span class="brand-sq" style="width:7px;height:7px"></span>Brankell Advisory</div>
  <h2 class="chapter-title" style="color:var(--blue)">Chapter Devider</h2>
  <div class="chapter-sub" style="color:var(--blue)">INTRODUCTION</div>
  <p class="chapter-text" style="color:var(--text)">Lorem ipsum dolor sit amet, consectetur adipiscing elit, sed do eiusmod tempor incididunt ut labore et dolore magna aliqua. Lorem ipsum dolor sit amet, consectetur adipiscing elit, sed do eiusmod tempor incididunt ut labore et dolore magna aliqua.</p>
</section>

<!-- 7 agenda -->
<section class="slide">
  <div class="agenda-panel">
    <h2 class="abs" style="left:23px;top:84px;margin:0;font-family:Poppins,sans-serif;font-weight:600;font-size:13px;line-height:1.3;color:#fff">Here Goes<br>Title Of Your<br>Agenda</h2>
    <div class="abs" style="left:23px;top:141px;font-size:4.5px;letter-spacing:1.3px;color:#fff">HERE GOES A SUBTITLE</div>
  </div>
  <ul class="agenda-list">
    <li><span>i.</span>Introduction</li>
    <li><span>ii.</span>About Us</li>
    <li><span>iii.</span>Welcome Message</li>
    <li><span>iv.</span>Company Profile</li>
    <li><span>v.</span>Team</li>
    <li><span>vi.</span>Team Group</li>
    <li><span>vii.</span>Portfolio</li>
    <li><span>viii.</span>Info graphic</li>
    <li><span>ix.</span>Contact Us</li>
  </ul>
</section>

<!-- 8 about -->
<section class="slide">
  <div class="photo" role="img" aria-label="Domed ceiling photograph with red and blue panels" style="left:0;top:0;width:165px;height:219px;background:radial-gradient(circle at 60% 50%,#3b4d6a,#6a2b38 45%,#1c2333)"></div>
  <div class="brand" style="left:38px;top:121px;font-size:10px;color:#fff"><span class="brand-sq" style="width:9px;height:9px"></span>Brankell Advisory</div>
  <h2 class="hero-title" style="left:195px;top:52px;font-size:17px;color:var(--blue)">Here Goes<br>Title Of This Slide</h2>
  <div class="abs" style="left:198px;top:112px;width:160px;font-size:6px;font-weight:700;color:var(--ink);line-height:1.2">Innovative EPM Solutions for Finance and Beyond</div>
  <p class="abs" style="left:198px;top:133px;width:170px;margin:0;font-size:4.6px;line-height:1.9;color:var(--text)">Brankell Advisory provides decades of experience implementing Veltrix Unified Results Planning with unique and innovative solutions to challenging business process not only in Finance and Accounting, but across organizations.</p>
</section>

<!-- 9 title + blank -->
<section class="slide">
  <span class="mark"></span><span class="vurl">WWW.BRANKELLADVISORY.EXAMPLE</span>
  <h2 class="title" style="left:32px;top:28px">Title + Blank</h2>
  <span class="pno">9</span>
</section>

<!-- 10 bullets -->
<section class="slide">
  <span class="mark"></span><span class="vurl">WWW.BRANKELLADVISORY.EXAMPLE</span>
  <h2 class="title" style="top:26px">Title + Content with nice bullets</h2>
  <div class="abs" style="left:28px;top:68px;width:144px">
    <p class="para">Business valuation is a process and a set of procedures used to estimate the economic value of an owner's interest in a business. Valuation is used by financial market participants to determine the price they are willing to pay or receive to effect a sale of a business.</p>
    <p class="para">In addition to estimating the selling price of a business, the same valuation tools are often used by business appraisers to resolve disputes related to estate and gift taxation, divorce litigation, allocate business purchase price among business assets, establish a formula for estimating the value of partners' ownership interest for buy-sell agreements, and many other business and legal purposes such as in shareholders deadlock, divorce litigation and estate contest.</p>
  </div>
  <ul class="bullets big abs" style="left:215px;top:70px;width:150px">
    <li>Lorem ipsum dolor sit amet, nec an dictas equidem appellantur, ut has commune accommodare. Mea illum, ludus solet idpro.</li>
    <li>Lorem ipsum dolor sit amet, nec an dictas equidem appellantur, ut has commune accommodare. Mea illum, ludus solet idpro.</li>
    <li>Lorem ipsum dolor sit amet, nec an dictas equidem appellantur, ut has commune accommodare. Mea illum, ludus solet idpro.</li>
    <li>Lorem ipsum dolor sit amet, nec an dictas equidem appellantur, ut has commune accommodare. Mea illum, ludus solet idpro.</li>
  </ul>
  <span class="pno">10</span>
</section>

<!-- 11 subtitle + bullets -->
<section class="slide">
  <span class="mark"></span><span class="vurl">WWW.BRANKELLADVISORY.EXAMPLE</span>
  <h2 class="title" style="top:18px">Title + SubTitle</h2>
  <div class="subtitle" style="left:29px;top:38px">SUBTITLE GOES HERE</div>
  <div class="cols" style="left:28px;top:68px;width:340px;gap:18px">
    <div>
      <p class="para">Lorem ipsum dolor sit amet, consectetur adipiscing elit, sed do eiusmod tempor incididunt ut labore et dolore magna aliqua. Ut enim ad minim veniam, quis nostrud exercitation ullamco laboris nisi ut aliquip ex. Lorem ipsum dolor sit amet, consectetur adipiscing elit, sed do eiusmod tempor incididunt ut labore et dolore magna aliqua.</p>
      <ul class="bullets small" style="margin-top:9px">
        <li>Lorem ipsum dolor sit amet, consectetur adipiscing</li>
        <li>Sed do eiusmod tempor incididunt ut labore et</li>
        <li>Dolore magna aliqua. Ut enim ad minim veniam</li>
        <li>Quis nostrud exercitation ullamco laboris nisi ut</li>
      </ul>
    </div>
    <div>
      <p class="para">Lorem ipsum dolor sit amet, consectetur adipiscing elit, sed do eiusmod tempor incididunt ut labore et dolore magna aliqua. Ut enim ad minim veniam, quis nostrud exercitation ullamco laboris nisi ut aliquip ex. Lorem ipsum dolor sit amet, consectetur adipiscing elit, sed do eiusmod tempor incididunt ut labore et dolore magna aliqua.</p>
      <ul class="bullets small" style="margin-top:9px">
        <li>Lorem ipsum dolor sit amet, consectetur adipiscing</li>
        <li>Sed do eiusmod tempor incididunt ut labore et</li>
        <li>Dolore magna aliqua. Ut enim ad minim veniam</li>
        <li>Quis nostrud exercitation ullamco laboris nisi ut</li>
      </ul>
    </div>
  </div>
  <span class="pno">11</span>
</section>

<!-- 12 two columns -->
<section class="slide">
  <span class="mark"></span><span class="vurl">WWW.BRANKELLADVISORY.EXAMPLE</span>
  <h2 class="title" style="left:32px;top:26px">Title + Two Columns of Content</h2>
  <div class="cols" style="left:32px;top:70px;width:340px;gap:28px">
    <div>
      <p class="para">Lorem ipsum dolor sit amet, consectetur adipiscing elit, sed do eiusmod tempor incididunt ut labore et dolore magna aliqua. Ut enim ad minim veniam, quis nostrud exercitation ullamco laboris nisi ut aliquip ex. Lorem ipsum dolor sit amet, consectetur adipiscing elit, sed do eiusmod tempor incididunt ut labore et dolore magna aliqua.</p>
      <p class="para">Lorem ipsum dolor sit amet, consectetur adipiscing elit, sed do eiusmod tempor incididunt ut labore et dolore magna aliqua. Ut enim ad minim veniam, quis nostrud exercitation ullamco laboris nisi ut aliquip ex. Lorem ipsum dolor sit amet, consectetur adipiscing elit, sed do eiusmod tempor incididunt ut labore et dolore magna aliqua.</p>
    </div>
    <div>
      <p class="para">Lorem ipsum dolor sit amet, consectetur adipiscing elit, sed do eiusmod tempor incididunt ut labore et dolore magna aliqua. Ut enim ad minim veniam, quis nostrud exercitation ullamco laboris nisi ut aliquip ex. Lorem ipsum dolor sit amet, consectetur adipiscing elit, sed do eiusmod tempor incididunt ut labore et dolore magna aliqua.</p>
      <p class="para">Lorem ipsum dolor sit amet, consectetur adipiscing elit, sed do eiusmod tempor incididunt ut labore et dolore magna aliqua. Ut enim ad minim veniam, quis nostrud exercitation ullamco laboris nisi ut aliquip ex. Lorem ipsum dolor sit amet, consectetur adipiscing elit, sed do eiusmod tempor incididunt ut labore et dolore magna aliqua.</p>
    </div>
  </div>
  <span class="pno">12</span>
</section>

<!-- 13 subtitle + two columns -->
<section class="slide">
  <span class="mark"></span><span class="vurl">WWW.BRANKELLADVISORY.EXAMPLE</span>
  <h2 class="title" style="left:30px;top:16px">Title + Subtitle + Two Columns</h2>
  <div class="subtitle" style="left:31px;top:37px">SUBTITLE GOES HERE</div>
  <div class="cols" style="left:30px;top:70px;width:342px;gap:28px">
    <div>
      <p class="para">Lorem ipsum dolor sit amet, consectetur adipiscing elit, sed do eiusmod tempor incididunt ut labore et dolore magna aliqua. Ut enim ad minim veniam, quis nostrud exercitation ullamco laboris nisi ut aliquip ex. Lorem ipsum dolor sit amet, consectetur adipiscing elit, sed do eiusmod tempor incididunt ut labore et dolore magna aliqua.</p>
      <p class="para">Lorem ipsum dolor sit amet, consectetur adipiscing elit, sed do eiusmod tempor incididunt ut labore et dolore magna aliqua. Ut enim ad minim veniam, quis nostrud exercitation ullamco laboris nisi ut aliquip ex. Lorem ipsum dolor sit amet, consectetur adipiscing elit, sed do eiusmod tempor incididunt ut labore et dolore magna aliqua.</p>
    </div>
    <div>
      <p class="para">Lorem ipsum dolor sit amet, consectetur adipiscing elit, sed do eiusmod tempor incididunt ut labore et dolore magna aliqua. Ut enim ad minim veniam, quis nostrud exercitation ullamco laboris nisi ut aliquip ex. Lorem ipsum dolor sit amet, consectetur adipiscing elit, sed do eiusmod tempor incididunt ut labore et dolore magna aliqua.</p>
      <p class="para">Lorem ipsum dolor sit amet, consectetur adipiscing elit, sed do eiusmod tempor incididunt ut labore et dolore magna aliqua. Ut enim ad minim veniam, quis nostrud exercitation ullamco laboris nisi ut aliquip ex. Lorem ipsum dolor sit amet, consectetur adipiscing elit, sed do eiusmod tempor incididunt ut labore et dolore magna aliqua.</p>
    </div>
  </div>
  <span class="pno">13</span>
</section>

<!-- 14 three cards -->
<section class="slide">
  <span class="mark"></span><span class="vurl">WWW.BRANKELLADVISORY.EXAMPLE</span>
  <h2 class="title center" style="top:28px">Title + Three Columns of Content</h2>
  <div class="card" style="left:41px;top:74px"><div class="icon"><svg width="14" height="14" viewBox="0 0 14 14"><circle cx="7" cy="7" r="5.5" fill="none" stroke="#fff" stroke-width="1.2"/><circle cx="7" cy="7" r="2" fill="#fff"/></svg></div><h4>Here is a place for text</h4><p class="para">Lorem ipsum dolor sit amet, nec an dictas equidem appellantur, ut has commune accommodare. Mea illum, ludus solet idpro.</p><p class="para">Lorem ipsum dolor sit amet, nec an dictas equidem appellantur, ut has commune accommodare. Mea illum, ludus solet idpro.</p></div>
  <div class="card" style="left:153px;top:74px"><div class="icon"><svg width="14" height="14" viewBox="0 0 14 14"><path d="M3 11 L11 3 M6 3 H11 V8" fill="none" stroke="#fff" stroke-width="1.4"/></svg></div><h4>Here is a place for text</h4><p class="para">Lorem ipsum dolor sit amet, nec an dictas equidem appellantur, ut has commune accommodare. Mea illum, ludus solet idpro.</p><p class="para">Lorem ipsum dolor sit amet, nec an dictas equidem appellantur, ut has commune accommodare. Mea illum, ludus solet idpro.</p></div>
  <div class="card" style="left:265px;top:74px"><div class="icon"><svg width="14" height="14" viewBox="0 0 14 14"><rect x="2" y="7" width="2.5" height="5" fill="#fff"/><rect x="5.8" y="4" width="2.5" height="8" fill="#fff"/><rect x="9.6" y="2" width="2.5" height="10" fill="#fff"/></svg></div><h4>Here is a place for text</h4><p class="para">Lorem ipsum dolor sit amet, nec an dictas equidem appellantur, ut has commune accommodare. Mea illum, ludus solet idpro.</p><p class="para">Lorem ipsum dolor sit amet, nec an dictas equidem appellantur, ut has commune accommodare. Mea illum, ludus solet idpro.</p></div>
  <span class="pno">14</span>
</section>

<!-- 15 subtitle + three cards -->
<section class="slide">
  <span class="mark"></span><span class="vurl">WWW.BRANKELLADVISORY.EXAMPLE</span>
  <h2 class="title center" style="top:17px">Title + Three Columns of Content</h2>
  <div class="subtitle center" style="top:38px">SUBTITLE GOES HERE</div>
  <div class="card" style="left:41px;top:74px"><div class="icon"><svg width="14" height="14" viewBox="0 0 14 14"><circle cx="7" cy="7" r="5.5" fill="none" stroke="#fff" stroke-width="1.2"/><circle cx="7" cy="7" r="2" fill="#fff"/></svg></div><h4>Here is a place for text</h4><p class="para">Lorem ipsum dolor sit amet, nec an dictas equidem appellantur, ut has commune accommodare. Mea illum, ludus solet idpro.</p><p class="para">Lorem ipsum dolor sit amet, nec an dictas equidem appellantur, ut has commune accommodare. Mea illum, ludus solet idpro.</p></div>
  <div class="card" style="left:153px;top:74px"><div class="icon"><svg width="14" height="14" viewBox="0 0 14 14"><path d="M3 11 L11 3 M6 3 H11 V8" fill="none" stroke="#fff" stroke-width="1.4"/></svg></div><h4>Here is a place for text</h4><p class="para">Lorem ipsum dolor sit amet, nec an dictas equidem appellantur, ut has commune accommodare. Mea illum, ludus solet idpro.</p><p class="para">Lorem ipsum dolor sit amet, nec an dictas equidem appellantur, ut has commune accommodare. Mea illum, ludus solet idpro.</p></div>
  <div class="card" style="left:265px;top:74px"><div class="icon"><svg width="14" height="14" viewBox="0 0 14 14"><rect x="2" y="7" width="2.5" height="5" fill="#fff"/><rect x="5.8" y="4" width="2.5" height="8" fill="#fff"/><rect x="9.6" y="2" width="2.5" height="10" fill="#fff"/></svg></div><h4>Here is a place for text</h4><p class="para">Lorem ipsum dolor sit amet, nec an dictas equidem appellantur, ut has commune accommodare. Mea illum, ludus solet idpro.</p><p class="para">Lorem ipsum dolor sit amet, nec an dictas equidem appellantur, ut has commune accommodare. Mea illum, ludus solet idpro.</p></div>
  <span class="pno">15</span>
</section>

<!-- 16 three text columns -->
<section class="slide">
  <span class="mark"></span><span class="vurl">WWW.BRANKELLADVISORY.EXAMPLE</span>
  <h2 class="title" style="left:30px;top:26px">Title + Three Columns of Content</h2>
  <div class="cols" style="left:30px;top:64px;width:342px;gap:22px">
    <div><p class="para">Lorem ipsum dolor sit amet, consectetur adipiscing elit, sed do eiusmod tempor incididunt ut labore et dolore magna aliqua. Lorem ipsum dolor sit amet, consectetur adipiscing elit.</p><p class="para">Sed do eiusmod tempor incididunt ut labore et dolore magna aliqua.</p><p class="para">Ut enim ad minim veniam, quis nostrud exercitation ullamco laboris nisi ut aliquip. Sed do eiusmod tempor incididunt ut labore et dolore magna aliqua.</p><p class="para">Ut enim ad minim veniam, quis nostrud exercitation ullamco laboris nisi ut aliquip.</p></div>
    <div><p class="para">Lorem ipsum dolor sit amet, consectetur adipiscing elit, sed do eiusmod tempor incididunt ut labore et dolore magna aliqua. Lorem ipsum dolor sit amet.</p><p class="para">Consectetur adipiscing elit, sed do eiusmod tempor incididunt ut labore et dolore magna aliqua. Ut enim ad minim veniam, quis nostrud exercitation ullamco laboris nisi ut aliquip.</p><p class="para">Consectetur adipiscing elit, sed do eiusmod tempor incididunt ut labore et dolore magna aliqua. Ut enim ad minim veniam, quis nostrud exercitation ullamco laboris nisi ut aliquip.</p></div>
    <div><p class="para">Lorem ipsum dolor sit amet, consectetur adipiscing elit, sed do eiusmod tempor incididunt ut labore et dolore magna aliqua.</p><p class="para">Consectetur adipiscing elit, sed do eiusmod tempor incididunt ut labore et dolore magna aliqua.</p><p class="para">Ut enim ad minim veniam, quis nostrud exercitation ullamco laboris nisi ut aliquip. Ut enim ad minim veniam, quis nostrud exercitation ullamco laboris nisi ut aliquip.</p></div>
  </div>
  <span class="pno">16</span>
</section>

<!-- 17 subtitle + three text columns -->
<section class="slide">
  <span class="mark"></span><span class="vurl">WWW.BRANKELLADVISORY.EXAMPLE</span>
  <h2 class="title" style="left:30px;top:16px">Title + Subtitle + Three Columns</h2>
  <div class="subtitle" style="left:31px;top:37px">SUBTITLE GOES HERE</div>
  <div class="cols" style="left:30px;top:64px;width:342px;gap:22px">
    <div><p class="para">Lorem ipsum dolor sit amet, consectetur adipiscing elit, sed do eiusmod tempor incididunt ut labore et dolore magna aliqua. Lorem ipsum dolor sit amet, consectetur adipiscing elit.</p><p class="para">Sed do eiusmod tempor incididunt ut labore et dolore magna aliqua.</p><p class="para">Ut enim ad minim veniam, quis nostrud exercitation ullamco laboris nisi ut aliquip. Sed do eiusmod tempor incididunt ut labore et dolore magna aliqua.</p><p class="para">Ut enim ad minim veniam, quis nostrud exercitation ullamco laboris nisi ut aliquip.</p></div>
    <div><p class="para">Lorem ipsum dolor sit amet, consectetur adipiscing elit, sed do eiusmod tempor incididunt ut labore et dolore magna aliqua. Lorem ipsum dolor sit amet.</p><p class="para">Consectetur adipiscing elit, sed do eiusmod tempor incididunt ut labore et dolore magna aliqua. Ut enim ad minim veniam, quis nostrud exercitation ullamco laboris nisi ut aliquip.</p><p class="para">Consectetur adipiscing elit, sed do eiusmod tempor incididunt ut labore et dolore magna aliqua. Ut enim ad minim veniam, quis nostrud exercitation ullamco laboris nisi ut aliquip.</p></div>
    <div><p class="para">Lorem ipsum dolor sit amet, consectetur adipiscing elit, sed do eiusmod tempor incididunt ut labore et dolore magna aliqua.</p><p class="para">Consectetur adipiscing elit, sed do eiusmod tempor incididunt ut labore et dolore magna aliqua.</p><p class="para">Ut enim ad minim veniam, quis nostrud exercitation ullamco laboris nisi ut aliquip. Ut enim ad minim veniam, quis nostrud exercitation ullamco laboris nisi ut aliquip.</p></div>
  </div>
  <span class="pno">17</span>
</section>

<!-- 18 two rows two columns -->
<section class="slide">
  <span class="mark"></span><span class="vurl">WWW.BRANKELLADVISORY.EXAMPLE</span>
  <h2 class="title" style="left:29px;top:28px">Title + Two Rows and Two Columns</h2>
  <div class="box" style="left:31px;top:74px"><h4>Project name</h4><p class="para">Lorem ipsum dolor sit amet, nec an dictas equidem appellantur, ut has commune accommodare. Mea illum, ludus solet idpro.</p></div>
  <div class="box gray" style="left:208px;top:74px"><h4>Project name</h4><p class="para">Lorem ipsum dolor sit amet, nec an dictas equidem appellantur, ut has commune accommodare. Mea illum, ludus solet idpro.</p></div>
  <div class="box" style="left:31px;top:133px"><h4>Project name</h4><p class="para">Lorem ipsum dolor sit amet, nec an dictas equidem appellantur, ut has commune accommodare. Mea illum, ludus solet idpro.</p></div>
  <div class="box gray" style="left:208px;top:133px"><h4>Project name</h4><p class="para">Lorem ipsum dolor sit amet, nec an dictas equidem appellantur, ut has commune accommodare. Mea illum, ludus solet idpro.</p></div>
  <span class="pno">18</span>
</section>

<!-- 19 two rows two columns table -->
<section class="slide">
  <span class="mark"></span><span class="vurl">WWW.BRANKELLADVISORY.EXAMPLE</span>
  <h2 class="title" style="left:31px;top:27px">Title + Two Rows and Two Columns</h2>
  <div class="split">
    <div class="head" style="background:var(--blue)">ADD YOUR TITLE</div>
    <div class="head" style="background:var(--navy)">ADD YOUR TITLE</div>
    <div class="cell"><h4>Project name</h4><p>Lorem ipsum is simply dummy unknown printer took a galley of type and scrambled it to make. Lorem ipsum is simply dummy unknown printer took a galley of type and scrambled it to make.</p></div>
    <div class="cell"><h4>Project name</h4><p>Lorem ipsum is simply dummy unknown printer took a galley of type and scrambled it to make. Lorem ipsum is simply dummy unknown printer took a galley of type and scrambled it to make.</p></div>
    <div class="cell"><h4>Project name</h4><p>Lorem ipsum is simply dummy unknown printer took a galley of type and scrambled it to make. Lorem ipsum is simply dummy unknown printer took a galley of type and scrambled it to make.</p></div>
    <div class="cell"><h4>Project name</h4><p>Lorem ipsum is simply dummy unknown printer took a galley of type and scrambled it to make. Lorem ipsum is simply dummy unknown printer took a galley of type and scrambled it to make.</p></div>
  </div>
  <span class="pno">19</span>
</section>

<!-- 20 nascar -->
<section class="slide">
  <span class="mark"></span><span class="vurl">WWW.BRANKELLADVISORY.EXAMPLE</span>
  <h2 class="title" style="left:47px;top:90px">Nascar Slide</h2>
  <p class="abs" style="left:40px;top:115px;width:130px;margin:0;font-size:4.4px;line-height:1.4;text-align:center;color:var(--text)">Lorem ipsum dolor sit amet, consectetur adipiscing elit, sed do eiusmod tempor incididunt ut labore et dolore magna aliqua. Lorem ipsum dolor sit amet, consectetur adipiscing elit.</p>
  <div class="client" style="left:190px;top:42px">Corvane</div>
  <div class="client" style="left:251px;top:42px">Haldrit</div>
  <div class="client" style="left:312px;top:42px">Vessora</div>
  <div class="client" style="left:190px;top:79px">Nimbla</div>
  <div class="client" style="left:251px;top:79px">Quorix</div>
  <div class="client" style="left:312px;top:79px">Ardeplace</div>
  <div class="client" style="left:190px;top:116px">Ensolo</div>
  <div class="client" style="left:251px;top:116px">Corvane</div>
  <div class="client" style="left:312px;top:116px">Tavelin</div>
  <div class="client" style="left:190px;top:153px">Haldrit</div>
  <div class="client" style="left:251px;top:153px">Lumora</div>
  <div class="client" style="left:312px;top:153px">Nimbla</div>
  <span class="pno">20</span>
</section>

<!-- 21 case study -->
<section class="slide">
  <span class="mark"></span><span class="vurl">WWW.BRANKELLADVISORY.EXAMPLE</span>
  <h2 class="title center" style="top:26px">Case Study Slide</h2>
  <div class="abs" style="left:0;right:0;top:64px;text-align:center;font-size:6.5px;font-weight:600;color:var(--blue)">Innovative EPM Solutions for Finance and Beyond</div>
  <p class="abs" style="left:40px;right:40px;top:80px;margin:0;text-align:center;font-size:4.6px;line-height:1.4;color:var(--text)">Brankell Advisory provides decades of experience implementing Veltrix Unified Results Planning with unique and innovative solutions to challenging business process not only in Finance and Accounting, but across organizations.</p>
  <div class="band" style="left:0;background:var(--blue)"><h4>Goal</h4><p>Lorem ipsum dolor sit amet, consectetur adipiscing elit, sed do eiusmod tempor incididunt ut labore et dolore magna aliqua.</p></div>
  <div class="band" style="left:130px;background:var(--navy)"><h4>Mission</h4><p>Lorem ipsum dolor sit amet, consectetur adipiscing elit, sed do eiusmod tempor incididunt ut labore et dolore magna aliqua.</p></div>
  <div class="band" style="left:260px;width:130px;background:var(--gray)"><h4>Vision</h4><p>Lorem ipsum dolor sit amet, consectetur adipiscing elit, sed do eiusmod tempor incididunt ut labore et dolore magna aliqua.</p></div>
  <div class="badge" style="left:18px;background:var(--blue)"><svg width="14" height="14" viewBox="0 0 14 14"><path d="M4 13 V2 L11 4.5 L4 7" fill="none" stroke="#fff" stroke-width="1.3"/></svg></div>
  <div class="badge" style="left:148px;background:var(--navy)"><svg width="14" height="14" viewBox="0 0 14 14"><path d="M3 11 L11 3 M6 3 H11 V8" fill="none" stroke="#fff" stroke-width="1.4"/></svg></div>
  <div class="badge" style="left:278px;background:var(--gray)"><svg width="16" height="14" viewBox="0 0 16 14"><circle cx="4.5" cy="8" r="3" fill="none" stroke="#fff" stroke-width="1.3"/><circle cx="11.5" cy="8" r="3" fill="none" stroke="#fff" stroke-width="1.3"/><path d="M7.5 8 H8.5" stroke="#fff" stroke-width="1.3"/></svg></div>
</section>

<!-- 22 table -->
<section class="slide">
  <span class="mark"></span><span class="vurl">WWW.BRANKELLADVISORY.EXAMPLE</span>
  <h2 class="title center" style="top:26px">Table</h2>
  <table class="grid-table">
    <tr><th class="blank"></th><th>Your Text Here</th><th>Your Text Here</th><th>Your Text Here</th><th>Your Text Here</th></tr>
    <tr><td class="label">You can replace this text</td><td>1250</td><td><svg width="8" height="7" viewBox="0 0 8 7"><path d="M1 3.5 L3 5.5 L7 1" fill="none" stroke="#1f74c0" stroke-width="1.4"/></svg></td><td>50%</td><td>1250</td></tr>
    <tr><td class="label">You can replace this text</td><td>3623</td><td><svg width="7" height="7" viewBox="0 0 7 7"><path d="M1 1 L6 6 M6 1 L1 6" stroke="#1f74c0" stroke-width="1.5"/></svg></td><td>50%</td><td>3623</td></tr>
    <tr><td class="label">You can replace this text</td><td>2569</td><td><svg width="8" height="7" viewBox="0 0 8 7"><path d="M1 3.5 L3 5.5 L7 1" fill="none" stroke="#1f74c0" stroke-width="1.4"/></svg></td><td>12%</td><td>2569</td></tr>
    <tr><td class="label">You can replace this text</td><td></td><td></td><td></td><td></td></tr>
    <tr><td class="label">You can replace this text</td><td></td><td></td><td></td><td></td></tr>
    <tr><td class="label">You can replace this text</td><td></td><td></td><td></td><td></td></tr>
  </table>
  <span class="pno">22</span>
</section>

<!-- 23 magnifier -->
<section class="slide">
  <span class="mark"></span><span class="vurl">WWW.BRANKELLADVISORY.EXAMPLE</span>
  <h2 class="title" style="left:30px;top:26px">Here Is A Place For Your Text</h2>
  <svg class="abs" style="left:0;top:60px" width="200" height="159" viewBox="0 0 200 159">
    <line x1="55" y1="95" x2="2" y2="135" stroke="#5c5e61" stroke-width="6" stroke-linecap="round"/>
    <circle cx="103" cy="65" r="54" fill="#fff" stroke="#3b4c84" stroke-width="3"/>
    <path d="M103 65 L103 18 A47 47 0 0 0 56 65 Z" fill="var(--blue)"/>
    <path d="M103 65 L150 65 A47 47 0 0 0 103 18 Z" fill="var(--gray)"/>
    <path d="M103 65 L56 65 A47 47 0 0 0 103 112 Z" fill="var(--gray)"/>
    <path d="M103 65 L103 112 A47 47 0 0 0 150 65 Z" fill="var(--blue)"/>
    <line x1="103" y1="16" x2="103" y2="114" stroke="#fff" stroke-width="2.5"/>
    <line x1="54" y1="65" x2="152" y2="65" stroke="#fff" stroke-width="2.5"/>
    <rect x="76" y="36" width="10" height="8" rx="1" fill="none" stroke="#fff" stroke-width="1"/>
    <circle cx="124" cy="40" r="4" fill="none" stroke="#fff" stroke-width="1"/>
    <circle cx="82" cy="88" r="4" fill="none" stroke="#fff" stroke-width="1"/>
    <rect x="119" y="84" width="10" height="9" rx="1" fill="none" stroke="#fff" stroke-width="1"/>
  </svg>
  <div class="step" style="top:62px"><span class="num">01</span><div><h4>Your Text Here</h4><p>You can simply impress your audience and add a unique zing and appeal to your Presentations. Easy to change colors, photos and Text.</p></div></div>
  <div class="step" style="top:96px"><span class="num">02</span><div><h4>Your Text Here</h4><p>You can simply impress your audience and add a unique zing and appeal to your Presentations. Easy to change colors, photos and Text.</p></div></div>
  <div class="step" style="top:130px"><span class="num">03</span><div><h4>Your Text Here</h4><p>You can simply impress your audience and add a unique zing and appeal to your Presentations. Easy to change colors, photos and Text.</p></div></div>
  <div class="step" style="top:164px"><span class="num">04</span><div><h4>Your Text Here</h4><p>You can simply impress your audience and add a unique zing and appeal to your Presentations. Easy to change colors, photos and Text.</p></div></div>
  <span class="pno">23</span>
</section>

<!-- 24 timeline -->
<section class="slide">
  <span class="mark"></span><span class="vurl">WWW.BRANKELLADVISORY.EXAMPLE</span>
  <h2 class="title center" style="top:26px">Timeline</h2>
  <div class="tl-label" style="left:33px;top:70px"><b>Your Title</b>Refers to a good or service being offered</div>
  <div class="tl-label" style="left:163px;top:70px"><b>Your Title</b>Refers to a good or service being offered</div>
  <div class="tl-label" style="left:293px;top:70px"><b>Your Title</b>Refers to a good or service being offered</div>
  <svg class="abs" style="left:30px;top:90px" width="340" height="50" viewBox="0 0 340 50">
    <g stroke="#1f74c0" stroke-width=".8"><line x1="38" y1="0" x2="38" y2="17"/><line x1="168" y1="0" x2="168" y2="17"/><line x1="298" y1="0" x2="298" y2="17"/></g>
    <g stroke="#27377a" stroke-width=".8"><line x1="103" y1="31" x2="103" y2="50"/><line x1="233" y1="31" x2="233" y2="50"/></g>
    <circle cx="38" cy="16" r="1.5" fill="#1f74c0"/><circle cx="168" cy="16" r="1.5" fill="#1f74c0"/><circle cx="298" cy="16" r="1.5" fill="#1f74c0"/>
    <polygon points="5,19 68,19 74,25 68,31 5,31 11,25" fill="#1f74c0"/>
    <polygon points="70,19 133,19 139,25 133,31 70,31 76,25" fill="#27377a"/>
    <polygon points="135,19 198,19 204,25 198,31 135,31 141,25" fill="#1f74c0"/>
    <polygon points="200,19 263,19 269,25 263,31 200,31 206,25" fill="#27377a"/>
    <polygon points="265,19 328,19 334,25 328,31 265,31 271,25" fill="#1f74c0"/>
    <g fill="#fff" font-family="Montserrat,sans-serif" font-size="5.5" font-weight="700" text-anchor="middle"><text x="38" y="27">1990</text><text x="103" y="27">2001</text><text x="168" y="27">2007</text><text x="233" y="27">2012</text><text x="298" y="27">2020</text></g>
  </svg>
  <div class="tl-label" style="left:98px;top:142px"><b>Your Title</b>Refers to a good or service being offered</div>
  <div class="tl-label" style="left:228px;top:142px"><b>Your Title</b>Refers to a good or service being offered</div>
  <span class="pno">24</span>
</section>

<!-- 25 nested circles -->
<section class="slide">
  <span class="mark"></span><span class="vurl">WWW.BRANKELLADVISORY.EXAMPLE</span>
  <h2 class="title" style="left:30px;top:26px">Here Is A Place For Your Text</h2>
  <svg class="abs" style="left:0;top:55px" width="240" height="164" viewBox="0 0 240 164">
    <circle cx="88" cy="82" r="55" fill="var(--navy)"/>
    <circle cx="88" cy="97" r="38" fill="var(--blue)"/>
    <circle cx="88" cy="120" r="17" fill="var(--gray)"/>
    <g fill="#fff" font-family="Poppins,sans-serif" font-size="11" font-weight="600" text-anchor="middle"><text x="88" y="52">$</text><text x="88" y="87">$</text><text x="88" y="124">$</text></g>
    <g stroke="#c8ccd2" stroke-width=".6"><line x1="105" y1="48" x2="170" y2="48"/><line x1="105" y1="83" x2="170" y2="83"/><line x1="105" y1="120" x2="170" y2="120"/></g>
  </svg>
  <div class="money" style="left:175px;top:96px">999M</div>
  <div class="money" style="left:175px;top:131px">99M</div>
  <div class="money" style="left:175px;top:168px">9M</div>
  <div class="check" style="top:94px"><svg width="14" height="12" viewBox="0 0 14 12"><path d="M1 6 L5 10 L13 2" fill="none" stroke="#1f74c0" stroke-width="2.4"/></svg><div><h4>Lorem ipsum dolor</h4><p>Lorem ipsum dolor sit amet, consectetur adipiscing elit, sed do eiusmod tempor</p></div></div>
  <div class="check" style="top:134px"><svg width="14" height="12" viewBox="0 0 14 12"><path d="M1 6 L5 10 L13 2" fill="none" stroke="#27377a" stroke-width="2.4"/></svg><div><h4>Lorem ipsum dolor</h4><p>Lorem ipsum dolor sit amet, consectetur adipiscing elit, sed do eiusmod tempor</p></div></div>
  <div class="check" style="top:174px"><svg width="14" height="12" viewBox="0 0 14 12"><path d="M1 6 L5 10 L13 2" fill="none" stroke="#6b6d70" stroke-width="2.4"/></svg><div><h4>Lorem ipsum dolor</h4><p>Lorem ipsum dolor sit amet, consectetur adipiscing elit, sed do eiusmod tempor</p></div></div>
  <span class="pno">25</span>
</section>

<!-- 26 main stage -->
<section class="slide">
  <span class="mark"></span><span class="vurl">WWW.BRANKELLADVISORY.EXAMPLE</span>
  <h2 class="title" style="left:30px;top:26px">Here Is A Place For Your Text</h2>
  <svg class="abs" style="left:0;top:0" width="390" height="219" viewBox="0 0 390 219">
    <g fill="none" stroke="#c5cad1" stroke-width=".7" stroke-dasharray="2 1.5">
      <path d="M115 79 H140 L165 100"/><path d="M115 118 H150"/><path d="M115 160 H140 L165 140"/>
      <path d="M275 79 H250 L225 100"/><path d="M275 118 H240"/><path d="M275 160 H250 L225 140"/>
    </g>
    <g fill="#c5cad1"><circle cx="115" cy="79" r="2"/><circle cx="115" cy="118" r="2"/><circle cx="115" cy="160" r="2"/><circle cx="275" cy="79" r="2"/><circle cx="275" cy="118" r="2"/><circle cx="275" cy="160" r="2"/></g>
  </svg>
  <div class="stage"></div>
  <div class="stage-text"><b>Main stage</b>dummy text of the printing<br>Of the printing and<br>typesetting</div>
  <div class="node left" style="left:35px;top:68px"><b>Main example</b>Is delivering creative solution through visual comunication</div>
  <div class="node left" style="left:35px;top:107px"><b>Main example</b>Is delivering creative solution through visual comunication</div>
  <div class="node left" style="left:35px;top:149px"><b>Main example</b>Is delivering creative solution through visual comunication</div>
  <div class="node right" style="left:280px;top:68px"><b>Main example</b>Is delivering creative solution through visual comunication</div>
  <div class="node right" style="left:280px;top:107px"><b>Main example</b>Is delivering creative solution through visual comunication</div>
  <div class="node right" style="left:280px;top:149px"><b>Main example</b>Is delivering creative solution through visual comunication</div>
  <span class="pno">26</span>
</section>

<!-- 27 ring -->
<section class="slide">
  <span class="mark"></span><span class="vurl">WWW.BRANKELLADVISORY.EXAMPLE</span>
  <h2 class="title" style="left:30px;top:26px">Here Is A Place For Your Text</h2>
  <svg class="abs" style="left:130px;top:63px" width="130" height="130" viewBox="0 0 130 130">
    <path d="M65 65 L65 6 A59 59 0 0 1 124 65 Z" fill="var(--blue)"/>
    <path d="M65 65 L124 65 A59 59 0 0 1 65 124 Z" fill="var(--navy)"/>
    <path d="M65 65 L65 124 A59 59 0 0 1 6 65 Z" fill="var(--blue)"/>
    <path d="M65 65 L6 65 A59 59 0 0 1 65 6 Z" fill="var(--navy)"/>
    <line x1="65" y1="4" x2="65" y2="126" stroke="#fff" stroke-width="2"/>
    <line x1="4" y1="65" x2="126" y2="65" stroke="#fff" stroke-width="2"/>
    <circle cx="65" cy="65" r="31" fill="#fff"/>
    <g fill="none" stroke="#fff" stroke-width="1.1"><circle cx="40" cy="38" r="6"/><circle cx="92" cy="38" r="6"/><circle cx="40" cy="92" r="6"/><circle cx="92" cy="92" r="6"/></g>
  </svg>
  <div class="brand" style="left:168px;top:122px;font-size:6px"><span class="brand-sq" style="width:6px;height:6px"></span>Brankell Advisory</div>
  <div class="side-note" style="left:37px;top:75px"><b>Your Contents Here</b>Lorem ipsum dolor sit amet, consectetur adipiscing elit, sed do eiusmod tempor incididunt.</div>
  <div class="side-note" style="left:37px;top:140px"><b>Your Contents Here</b>Lorem ipsum dolor sit amet, consectetur adipiscing elit, sed do eiusmod tempor incididunt.</div>
  <div class="side-note" style="left:270px;top:72px;text-align:left"><b>Your Contents Here</b>Lorem ipsum dolor sit amet, consectetur adipiscing elit, sed do eiusmod tempor incididunt.</div>
  <div class="side-note" style="left:270px;top:137px;text-align:left"><b>Your Contents Here</b>Lorem ipsum dolor sit amet, consectetur adipiscing elit, sed do eiusmod tempor incididunt.</div>
  <span class="pno">27</span>
</section>

<!-- 28 triangles -->
<section class="slide">
  <span class="mark"></span><span class="vurl">WWW.BRANKELLADVISORY.EXAMPLE</span>
  <h2 class="title" style="left:30px;top:26px">Here Is A Place For Your Text</h2>
  <div class="item" style="left:38px;top:68px"><span class="ic" style="background:var(--blue);box-shadow:0 0 0 2px #d6e4f3"><svg width="11" height="11" viewBox="0 0 11 11"><circle cx="5.5" cy="5.5" r="4" fill="none" stroke="#fff"/><circle cx="5.5" cy="5.5" r="1.5" fill="#fff"/></svg></span><div><h4>Project name</h4><p>Lorem ipsum dolor sit amet, nec an dictas equidem appellantur, ut has commune accommodare. Mea illum, ludus solet idpro.</p></div></div>
  <div class="item" style="left:38px;top:110px"><span class="ic" style="background:var(--navy);box-shadow:0 0 0 2px #d7dae8"><svg width="11" height="11" viewBox="0 0 11 11"><path d="M2 9 L9 2 M5 2 H9 V6" fill="none" stroke="#fff" stroke-width="1.2"/></svg></span><div><h4>Project name</h4><p>Lorem ipsum dolor sit amet, nec an dictas equidem appellantur, ut has commune accommodare. Mea illum, ludus solet idpro.</p></div></div>
  <div class="item" style="left:38px;top:152px"><span class="ic" style="background:var(--gray);box-shadow:0 0 0 2px #e0e1e3"><svg width="11" height="11" viewBox="0 0 11 11"><rect x="2" y="2" width="7" height="7" fill="none" stroke="#fff"/></svg></span><div><h4>Project name</h4><p>Lorem ipsum dolor sit amet, nec an dictas equidem appellantur, ut has commune accommodare. Mea illum, ludus solet idpro.</p></div></div>
  <svg class="abs" style="left:0;top:0" width="390" height="219" viewBox="0 0 390 219">
    <polygon points="295,58 255,127 335,127" fill="var(--blue)"/>
    <polygon points="252,133 212,202 292,202" fill="var(--navy)"/>
    <polygon points="338,133 298,202 378,202" fill="var(--gray)"/>
  </svg>
  <div class="tri-text" style="left:268px;top:84px"><b>Project name</b>Lorem ipsum dolor sit amet, nec an dictas equidem appellantur, ut has commune accommodare.</div>
  <div class="tri-text" style="left:225px;top:165px"><b>Project name</b>Lorem ipsum dolor sit amet, nec an dictas equidem appellantur, ut has commune accommodare.</div>
  <div class="tri-text" style="left:311px;top:165px"><b>Project name</b>Lorem ipsum dolor sit amet, nec an dictas equidem appellantur, ut has commune accommodare.</div>
  <span class="pno">28</span>
</section>

<!-- 29 brand circle list -->
<section class="slide">
  <span class="mark"></span><span class="vurl">WWW.BRANKELLADVISORY.EXAMPLE</span>
  <h2 class="title" style="left:30px;top:26px">Here Is A Place For Your Text</h2>
  <div class="abs" style="left:39px;top:85px;width:86px;height:86px;border-radius:50%;background:var(--blue);box-shadow:0 0 0 4px #d7e5f4"></div>
  <div class="brand" style="left:49px;top:124px;font-size:6.5px;color:#fff"><span class="brand-sq" style="width:6px;height:6px"></span>Brankell Advisory</div>
  <div class="item" style="left:175px;top:68px;width:190px"><span class="ic" style="background:#5a5c60;box-shadow:0 0 0 2px #e0e1e3"><svg width="11" height="11" viewBox="0 0 11 11"><circle cx="5.5" cy="5.5" r="3.5" fill="none" stroke="#fff"/></svg></span><div><h4>Project name</h4><p>Lorem ipsum dolor sit amet, nec an dictas equidem appellantur, ut has commune accommodare. Mea illum, ludus solet idpro.</p></div></div>
  <div class="item" style="left:175px;top:112px;width:190px"><span class="ic" style="background:#5a5c60;box-shadow:0 0 0 2px #e0e1e3"><svg width="11" height="11" viewBox="0 0 11 11"><rect x="1.5" y="2" width="8" height="5.5" fill="none" stroke="#fff"/><line x1="5.5" y1="7.5" x2="5.5" y2="9.5" stroke="#fff"/></svg></span><div><h4>Project name</h4><p>Lorem ipsum dolor sit amet, nec an dictas equidem appellantur, ut has commune accommodare. Mea illum, ludus solet idpro.</p></div></div>
  <div class="item" style="left:175px;top:156px;width:190px"><span class="ic" style="background:#5a5c60;box-shadow:0 0 0 2px #e0e1e3"><svg width="11" height="11" viewBox="0 0 11 11"><rect x="2" y="2" width="7" height="7" fill="none" stroke="#fff"/></svg></span><div><h4>Project name</h4><p>Lorem ipsum dolor sit amet, nec an dictas equidem appellantur, ut has commune accommodare. Mea illum, ludus solet idpro.</p></div></div>
  <span class="pno">29</span>
</section>

<!-- 30 contact -->
<section class="slide" style="background:linear-gradient(120deg,#f6f7f8,#eceef1)">
  <div class="contact-card">
    <div class="row lead"><svg width="8" height="8" viewBox="0 0 8 8"><circle cx="4" cy="4" r="3.3" fill="none" stroke="#fff" stroke-width=".8"/><path d="M.7 4 H7.3 M4 .7 C2 3 2 5 4 7.3 M4 .7 C6 3 6 5 4 7.3" fill="none" stroke="#fff" stroke-width=".6"/></svg>www.brankelladvisory.example</div>
    <div class="row" style="height:28px"><svg width="7" height="9" viewBox="0 0 7 9"><path d="M3.5 8.5 C1 5.5 .5 4.5 .5 3.5 A3 3 0 0 1 6.5 3.5 C6.5 4.5 6 5.5 3.5 8.5 Z" fill="none" stroke="#1f74c0" stroke-width=".9"/></svg><span style="line-height:1.4">Here to write your<br>Company adress</span></div>
    <div class="row" style="height:28px"><svg width="8" height="8" viewBox="0 0 8 8"><path d="M1.5 .8 L3 .8 L3.6 2.6 L2.6 3.4 C3.1 4.5 3.6 5 4.6 5.4 L5.4 4.4 L7.2 5 L7.2 6.5 C7.2 7 6.8 7.3 6.3 7.3 C3.2 7 1 4.8 .7 1.7 C.7 1.2 1 .8 1.5 .8 Z" fill="#1f74c0"/></svg>(555) 010-0142</div>
    <div class="row" style="height:28px;border-bottom:0"><svg width="9" height="7" viewBox="0 0 9 7"><rect x=".5" y=".5" width="8" height="6" fill="#1f74c0"/><path d="M.5 .5 L4.5 4 L8.5 .5" fill="none" stroke="#fff" stroke-width=".7"/></svg>info@brankelladvisory.example</div>
  </div>
  <div class="socials"><span></span><span></span><span></span><span></span></div>
  <div class="brand" style="left:222px;top:116px;font-size:15px"><span class="brand-sq" style="width:13px;height:13px"></span>Brankell Advisory</div>
</section>

</main>
</body>
</html>
```